Harbor Crest Vitality.com Landing Page

Create a well designed home/landing page using that communicates the feeling of Harbor Crest Vitality with this sections that scroll from top to bottom -
Top section - Displays "Harbor Crest Vitality" with space for embedded YouTube video.

The following sections follow the top section -
Assess your current Harbor Crest Vitality. Complete our free life balance assessment to identify key areas where you you will most benefit.
"Learn more" call to action button

Create a Harbor Crest Vitality Learning Portal account. Get a 14 day free trial to a wealth of learning activities, motivational videos and professional presentations on our learning portal designed specifically to address the eight essential areas of Harbor Crest Vitality.
"Register now" call to action button

Get weekly reports on your progress and goal achievement. Celebrate your success each week as you review your progress on each life balance area.

Appropriate royalty free photos and graphics that fit the chosen theme you recommend.

I'm reviewing the designs. I realize that I need to clarify that Harbor Crest Vitality focuses on eight areas, not just physical fitness and meditation. Spirituality and Sense of Purpose; Fitness and Health; Relationships; Personal Finance; Recreation and Fun; Physical Environment; Personal Development and Learning; Work and Career

1 page

33a6d7
00a990
9bcb3c
2f73b3

```html
<!DOCTYPE html>
<html lang="en">
<head>
<meta charset="utf-8">
<title>Harbor Crest Vitality</title>
<link rel="stylesheet" href="https://fonts.googleapis.com/css2?family=Quicksand:wght@500;600;700&display=swap">
<style>
:root{
  --blue:#33a6d7;
  --teal:#00a990;
  --green:#9bcb3c;
  --green-deep:#86c232;
  --navy:#2f73b3;
  --ink:#333333;
  --muted:#555555;
  --rule:#e6e6e6;
  --footer:#1d1d1d;
  --star:#f29c1f;
}
*{box-sizing:border-box;margin:0;padding:0}
html,body{width:1200px;height:4085px;overflow:hidden;background:#fff}
body{font-family:'Quicksand',sans-serif;color:var(--ink);position:relative}
.abs{position:absolute}

/* header + hero */
.hero{left:0;top:0;width:1200px;height:800px}
.hero-photo{left:0;top:0;width:1200px;height:800px;
  background:linear-gradient(180deg,#dfe7ee 0%,#c9d6e0 30%,#9fb7cd 48%,#4f82b3 60%,#6d97c1 80%,#b9cde0 100%)}
.header{left:0;top:0;width:1200px;height:125px;background:rgba(255,255,255,.55)}
.brand{left:110px;top:28px;font-size:31px;font-weight:600;color:var(--blue);line-height:34px}
.brand .line2{display:block;text-align:right;font-size:25px}
.nav{top:60px;right:112px;display:flex;gap:52px;font-size:13px;font-weight:600;color:#222}
.nav a{color:inherit;text-decoration:none}
.nav .active{color:var(--blue)}
.hero-title{left:0;width:1200px;top:186px;text-align:center;font-size:52px;font-weight:600;letter-spacing:.5px}
.hero-title .g{color:var(--green-deep)}
.hero-title .b{color:var(--blue)}
.video-slot{left:561px;top:262px;width:78px;height:54px;border-radius:14px;background:#e3262a}

/* welcome */
.welcome{left:0;width:1200px;top:818px;text-align:center}
.welcome h2{font-size:38px;font-weight:500;color:#333;line-height:1.2}
.welcome h3{font-size:42px;font-weight:500;color:var(--green-deep);line-height:1.25}
.welcome p{width:680px;margin:34px auto 0;font-family:Arial,sans-serif;font-size:13.5px;line-height:31px;color:var(--muted)}
.btn{display:flex;align-items:center;justify-content:center;border-radius:30px;color:#fff;font-size:18px;font-weight:600}
.btn-grad{left:488px;top:1130px;width:224px;height:60px;font-size:20px;background:linear-gradient(90deg,var(--blue),var(--green))}

/* feature rows */
.frame{width:240px;height:185px}
.photo{width:462px;height:347px}
.feature-text{font-size:18px;line-height:35px;color:#333;font-weight:500}
.rule{left:110px;width:980px;height:1px;background:var(--rule)}

/* band */
.band{left:0;top:2619px;width:1200px;height:549px;background:linear-gradient(90deg,#3fa3d6 0%,#4bb1a7 45%,#8cc442 100%)}
.band-title{left:0;width:1200px;top:2678px;text-align:center;color:#fff;font-weight:500}
.band-title .l1{font-size:30px;display:block}
.band-title .l2{font-size:38px;display:block;margin-top:6px}
.card{top:2806px;width:232px;height:287px;background:#fff;border-radius:8px;text-align:center}
.card svg{margin-top:30px}
.card h4{font-size:18px;font-weight:600;color:#222;margin-top:14px}
.card .dash{width:34px;height:2px;background:var(--green);margin:12px auto 0}
.card p{font-family:Arial,sans-serif;font-size:13px;line-height:26px;color:#666;margin:10px 20px 0}

/* testimonials */
.t-title{left:0;width:1200px;top:3230px;text-align:center;font-size:34px;font-weight:500}
.t-title span{color:var(--green-deep)}
.t-line{left:582px;top:3290px;width:36px;height:2px;background:var(--green)}
.trainee{top:3335px;width:300px;text-align:center}
.avatar{width:185px;height:185px;border-radius:50%;margin:0 auto}
.stars{color:var(--star);font-size:15px;letter-spacing:2px;margin-top:18px}
.trainee h5{font-size:20px;font-weight:500;margin-top:4px;color:#222}
.trainee p{font-family:Arial,sans-serif;font-size:13px;line-height:26px;color:#666;margin:12px 40px 0}

/* footer */
.footer-shape{left:0;top:3730px;width:1200px;height:355px}
.f-item{top:3846px;width:320px;text-align:center;color:#fff;font-size:16px;line-height:27px}
.f-icon{width:52px;height:52px;border:2px solid #fff;border-radius:50%;margin:0 auto 20px;display:flex;align-items:center;justify-content:center}
.copyright{left:0;width:1200px;top:4030px;text-align:center;font-family:Arial,sans-serif;font-size:12px;color:#fff}
</style>
</head>
<body>

<section class="hero abs">
  <div class="hero-photo abs" role="img" aria-label="Woman meditating cross-legged by a calm sea with distant mountains and soft clouds"></div>
  <svg class="abs" style="left:0;top:700px" width="1200" height="100" viewBox="0 0 1200 100">
    <polygon points="0,80 1200,10 1200,100 0,100" fill="#fff"/>
    <polygon points="640,45 1200,12 1200,92" fill="var(--green-deep)"/>
  </svg>
  <header class="header abs">
    <div class="brand abs">Harbor Crest<span class="line2">Vitality</span></div>
    <nav class="nav abs">
      <a class="active">HOME</a><a>ABOUT US</a><a>SERVICES</a><a>NEWS</a><a>CONTACT US</a>
    </nav>
  </header>
  <h1 class="hero-title abs"><span class="g">HARBOR CREST</span> <span class="b">VITALITY</span></h1>
  <div class="video-slot abs" role="img" aria-label="Embedded video placeholder"></div>
</section>

<section class="welcome abs">
  <h2>Welcome to</h2>
  <h3>Harbor Crest Vitality</h3>
  <p>Giving you hope, inspiring you to take action and providing you with the tools and strategies to succeed. Proven principles you can practice to achieve and keep life balance.Giving you hope, inspiring you to take action and providing you with the tools and strategies to succeed. Proven principles you can practice to achieve and keep life balance.Sed ut perspiciatis unde omnis iste natus error sit voluptatem accusantium unde omnis iste natus omnis iste natus error doloremque laudantium</p>
</section>
<div class="btn btn-grad abs">Learn More</div>

<!-- feature 1 -->
<div class="frame abs" style="left:110px;top:1260px;background:var(--green-deep)"></div>
<div class="photo abs" style="left:120px;top:1268px;background:linear-gradient(135deg,#a8c5a0,#4f6a55 55%,#3b4c63)" role="img" aria-label="Woman relaxing on a balcony with eyes closed"></div>
<p class="feature-text abs" style="left:648px;top:1335px;width:420px">Assess your current Harbor Crest Vitality. Complete our free life balance assessment to identify key areas where you you will most benefit.</p>
<div class="btn abs" style="left:646px;top:1500px;width:181px;height:58px;background:var(--green-deep)">Learn More</div>
<div class="rule abs" style="top:1665px"></div>

<!-- feature 2 -->
<div class="frame abs" style="left:850px;top:1707px;background:var(--blue)"></div>
<div class="photo abs" style="left:616px;top:1717px;background:linear-gradient(160deg,#b7d0e4,#d6d0c0 50%,#b69a6a)" role="img" aria-label="Woman with arms raised on a grassy seaside cliff"></div>
<p class="feature-text abs" style="left:128px;top:1767px;width:449px;text-align:justify">Create a Harbor Crest Vitality Learning Portal account. Get a 14 day free trial to a wealth of learning activities, motivational videos and professional presentations on our learning portal designed specifically to address the eight essential areas of Harbor Crest Vitality.</p>
<div class="btn abs" style="left:127px;top:2003px;width:181px;height:58px;background:var(--blue)">Register Now</div>
<div class="rule abs" style="top:2115px"></div>

<!-- feature 3 -->
<div class="frame abs" style="left:110px;top:2172px;background:var(--teal)"></div>
<div class="photo abs" style="left:120px;top:2180px;background:linear-gradient(135deg,#6b7a3a,#c9b24a 50%,#e9d27a)" role="img" aria-label="Person meditating in sunlit grass with a butterfly on the hand"></div>
<p class="feature-text abs" style="left:648px;top:2247px;width:420px">Get weekly reports on your progress and goal achievement. Celebrate your success each week as you review your progress on each life balance area</p>
<div class="btn abs" style="left:646px;top:2411px;width:181px;height:58px;background:var(--teal)">Learn More</div>

<!-- six things -->
<section class="band abs" role="img" aria-label="Soft blue to green tinted backdrop"></section>
<h2 class="band-title abs"><span class="l1">The Six Things That</span><span class="l2">Happen When You Meet Me</span></h2>

<div class="card abs" style="left:111px">
  <svg width="84" height="84" viewBox="0 0 84 84" fill="none" stroke="var(--teal)" stroke-width="3" stroke-linecap="round" stroke-linejoin="round">
    <path d="M10 78 C8 50 18 24 30 8 L44 10 L42 20 L34 22 L28 44 C40 34 58 36 66 48 C74 60 66 76 50 78 Z"/>
    <path d="M60 70 L78 70"/>
  </svg>
  <h4>Building strength</h4><div class="dash"></div>
  <p>Sed ut perspiciatis unde omnis iste natus error sit volupta accu santium dolorem</p>
</div>
<div class="card abs" style="left:360px">
  <svg width="84" height="84" viewBox="0 0 84 84" fill="none" stroke="var(--teal)" stroke-width="3" stroke-linecap="round" stroke-linejoin="round">
    <rect x="6" y="26" width="56" height="44" rx="3"/>
    <circle cx="30" cy="44" r="8"/><path d="M16 70 C18 58 42 58 44 70"/>
    <rect x="52" y="6" width="26" height="18" rx="3"/><path d="M58 13h14M58 18h10"/>
    <path d="M2 78h80"/>
  </svg>
  <h4>Learning on the go</h4><div class="dash"></div>
  <p>Sed ut perspiciatis unde omnis iste natus error sit volupta accu santium dolorem</p>
</div>
<div class="card abs" style="left:608px">
  <svg width="84" height="84" viewBox="0 0 84 84" fill="none" stroke="var(--teal)" stroke-width="3" stroke-linecap="round">
    <path d="M40 8 C24 6 10 18 12 32 C4 40 6 58 18 62 C20 76 34 80 40 74 Z"/>
    <path d="M44 8 C60 6 74 18 72 32 C80 40 78 58 66 62 C64 76 50 80 44 74 Z"/>
    <circle cx="28" cy="36" r="7"/><circle cx="56" cy="48" r="7"/><circle cx="30" cy="58" r="4"/><circle cx="56" cy="24" r="4"/>
  </svg>
  <h4>Fixing the mindset</h4><div class="dash"></div>
  <p>Sed ut perspiciatis unde omnis iste natus error sit volupta accu santium dolorem</p>
</div>
<div class="card abs" style="left:856px">
  <svg width="84" height="84" viewBox="0 0 84 84" fill="none" stroke="var(--teal)" stroke-width="3" stroke-linecap="round">
    <path d="M42 6 V34 M42 34 L34 42 M42 34 L50 42"/>
    <path d="M34 26 C20 12 4 30 4 56 C4 74 20 78 34 70 Z"/>
    <path d="M50 26 C64 12 80 30 80 56 C80 74 64 78 50 70 Z"/>
    <circle cx="18" cy="52" r="2" fill="var(--teal)"/><circle cx="24" cy="62" r="2" fill="var(--teal)"/>
    <circle cx="64" cy="50" r="2" fill="var(--teal)"/><circle cx="60" cy="62" r="2" fill="var(--teal)"/>
  </svg>
  <h4>Improve your lungs</h4><div class="dash"></div>
  <p>Sed ut perspiciatis unde omnis iste natus error sit volupta accu santium dolorem</p>
</div>

<!-- testimonials -->
<h2 class="t-title abs">My <span>Trainees Say</span></h2>
<div class="t-line abs"></div>

<div class="trainee abs" style="left:121px">
  <div class="avatar" style="background:linear-gradient(160deg,#c98a5e,#7d4a36)" role="img" aria-label="Portrait of trainee Mara Lindqvist"></div>
  <div class="stars">☆☆☆☆☆</div>
  <h5>Mara Lindqvist</h5>
  <p>I just love you Jo, you fixed my life and made me a better person. How did you do it?</p>
</div>
<div class="trainee abs" style="left:454px">
  <div class="avatar" style="background:linear-gradient(160deg,#bdbdbd,#5b5b5b)" role="img" aria-label="Portrait of trainee Owen Castell"></div>
  <div class="stars">☆☆☆☆☆</div>
  <h5>Owen Castell</h5>
  <p>I'm someone who struggled with weight. Jo helped me get in better shape.</p>
</div>
<div class="trainee abs" style="left:788px">
  <div class="avatar" style="background:linear-gradient(160deg,#6f7d5a,#2f2f2f)" role="img" aria-label="Portrait of trainee Priya Desmond"></div>
  <div class="stars">☆☆☆☆☆</div>
  <h5>Priya Desmond</h5>
  <p>Now I am fit like the girls you see on Brightwave TV. While that wasn't my now I'm really into it.</p>
</div>

<!-- footer -->
<svg class="footer-shape abs" viewBox="0 0 1200 355" preserveAspectRatio="none">
  <polygon points="0,0 390,60 1200,18 1200,355 0,355" fill="var(--footer)"/>
  <polygon points="0,0 390,60 0,80" fill="var(--green-deep)"/>
</svg>

<div class="f-item abs" style="left:112px">
  <div class="f-icon"><svg width="18" height="22" viewBox="0 0 18 22"><path d="M9 1C4.6 1 1 4.4 1 8.8 1 14 9 21 9 21s8-7 8-12.2C17 4.4 13.4 1 9 1z" fill="none" stroke="#fff" stroke-width="2"/><circle cx="9" cy="8.5" r="2.5" fill="#fff"/></svg></div>
  #14 Lorem Ipsum Dummy text<br>Lorem Ipum dummy
</div>
<div class="f-item abs" style="left:435px">
  <div class="f-icon"><svg width="20" height="20" viewBox="0 0 24 24"><path d="M6.6 10.8c1.4 2.8 3.8 5.1 6.6 6.6l2.2-2.2c.3-.3.7-.4 1-.2 1.1.4 2.3.6 3.6.6.6 0 1 .4 1 1V20c0 .6-.4 1-1 1C10.6 21 3 13.4 3 4c0-.6.4-1 1-1h3.5c.6 0 1 .4 1 1 0 1.3.2 2.5.6 3.6.1.3 0 .7-.2 1l-2.3 2.2z" fill="#fff"/></svg></div>
  Phone :<br>555-014-2290
</div>
<div class="f-item abs" style="left:758px">
  <div class="f-icon"><svg width="22" height="16" viewBox="0 0 22 16"><rect x="0" y="0" width="22" height="16" rx="2" fill="#fff"/><path d="M1 1l10 8 10-8" fill="none" stroke="var(--footer)" stroke-width="2"/></svg></div>
  Email :<br>hello@harborcrestvitality.com
</div>

<p class="copyright abs">© Copyright 2020 Harbor Crest Vitality.All Rights Reserved</p>

</body>
</html>
```